Corvane Property Group Business cards

I am starting a property development and consultancy business called Corvane Property Group. I have a logo designed and a website on its way:
www.corvanegroup-example.com.au

I need a business card with the following:

Front:
Mostly orange with logo taking up all front of card

Back of card:
Logo

Mark Dellaway
Managing Director

T +61 452 907 364
E mark.dellaway@corvanegroup-example.com.au
www.corvanegroup-example.com.au

Industry/Entity Type

Business

Requirements
Must have
• curved edges

```html
<!DOCTYPE html>
<html lang="en">
<head>
<meta charset="utf-8">
<title>Corvane Property Group — Business Cards</title>
<link rel="stylesheet" href="https://fonts.googleapis.com/css2?family=Open+Sans:wght@400;600;700&display=swap">
<style>
  :root {
    --orange: #f2a81d;
    --orange-deep: #e89a12;
    --paper: #ffffff;
    --paper-shade: #f1f1f1;
    --ink: #3a3a3a;
    --ink-soft: #555555;
    --rule: #9a9a9a;
    --band-line: #444444;
    --backdrop: #5b5b5b;
  }
  * { box-sizing: border-box; margin: 0; padding: 0; }
  html, body { width: 1200px; height: 900px; overflow: hidden; }
  body {
    background: var(--backdrop);
    font-family: "Open Sans", Arial, sans-serif;
    position: relative;
  }
  .card {
    position: absolute;
    left: 250px;
    width: 700px;
    height: 400px;
    border-radius: 22px;
    overflow: hidden;
  }

  /* Front: brand name fills the orange face */
  .card-front {
    top: 40px;
    background: linear-gradient(135deg, var(--orange) 0%, var(--orange-deep) 100%);
    display: flex;
    align-items: center;
    justify-content: center;
  }
  .front-brand {
    color: var(--paper);
    font-weight: 600;
    text-transform: uppercase;
    text-align: center;
    line-height: 1.1;
  }
  .front-brand .word-main { display: block; font-size: 84px; letter-spacing: 8px; }
  .front-brand .word-sub { display: block; font-size: 26px; letter-spacing: 14px; margin-top: 10px; }

  /* Back */
  .card-back {
    top: 470px;
    background: linear-gradient(160deg, var(--paper) 0%, var(--paper) 55%, var(--paper-shade) 100%);
  }
  .brand {
    position: absolute;
    left: 48px;
    top: 70px;
    display: flex;
    align-items: center;
    gap: 14px;
  }
  .brand-square {
    width: 46px;
    height: 46px;
    background: var(--orange);
  }
  .brand-name {
    color: var(--ink);
    font-weight: 600;
    text-transform: uppercase;
    line-height: 1.1;
  }
  .brand-name .word-main { display: block; font-size: 38px; letter-spacing: 3px; }
  .brand-name .word-sub { display: block; font-size: 15px; letter-spacing: 5px; }

  .person {
    position: absolute;
    right: 40px;
    top: 96px;
    text-align: right;
  }
  .person-name { color: var(--orange-deep); font-weight: 700; font-size: 19px; }
  .person-title { color: var(--ink); font-size: 14px; margin-top: 2px; }

  .divider {
    position: absolute;
    left: 48px;
    right: 34px;
    top: 172px;
    height: 1px;
    background: var(--rule);
  }

  .contacts {
    position: absolute;
    left: 48px;
    top: 205px;
    list-style: none;
  }
  .contacts li {
    display: flex;
    align-items: center;
    gap: 18px;
    height: 32px;
    font-size: 16px;
    color: var(--ink-soft);
  }
  .contact-icon {
    width: 20px;
    height: 20px;
    background: var(--orange);
    display: flex;
    align-items: center;
    justify-content: center;
  }
  .contact-icon svg { width: 14px; height: 14px; }

  .band-line {
    position: absolute;
    left: 0; right: 0;
    bottom: 30px;
    height: 3px;
    background: var(--band-line);
  }
  .band {
    position: absolute;
    left: 0; right: 0;
    bottom: 0;
    height: 24px;
    background: var(--orange);
  }
</style>
</head>
<body>

  <section class="card card-front" aria-label="Card front">
    <div class="front-brand">
      <span class="word-main">Corvane</span>
      <span class="word-sub">Property Group</span>
    </div>
  </section>

  <section class="card card-back" aria-label="Card back">
    <div class="brand">
      <div class="brand-square"></div>
      <div class="brand-name">
        <span class="word-main">Corvane</span>
        <span class="word-sub">Property Group</span>
      </div>
    </div>

    <div class="person">
      <div class="person-name">Mark Dellaway</div>
      <div class="person-title">Managing Director</div>
    </div>

    <div class="divider"></div>

    <ul class="contacts">
      <li>
        <span class="contact-icon">
          <svg viewBox="0 0 24 24" fill="none" stroke="#fff" stroke-width="2.4" stroke-linecap="round" stroke-linejoin="round"><path d="M5 3h4l2 5-3 2a12 12 0 0 0 6 6l2-3 5 2v4a2 2 0 0 1-2 2A17 17 0 0 1 3 5a2 2 0 0 1 2-2z"/></svg>
        </span>
        +61 452 907 364
      </li>
      <li>
        <span class="contact-icon">
          <svg viewBox="0 0 24 24" fill="none" stroke="#fff" stroke-width="2.4" stroke-linecap="round"><circle cx="12" cy="12" r="4"/><path d="M16 8v5a3 3 0 0 0 6 0v-1a10 10 0 1 0-4 8"/></svg>
        </span>
        mark.dellaway@corvanegroup-example.com.au
      </li>
      <li>
        <span class="contact-icon">
          <svg viewBox="0 0 24 24" fill="none" stroke="#fff" stroke-width="2.2"><circle cx="12" cy="12" r="9"/><path d="M3 12h18M12 3c3 3 3 15 0 18M12 3c-3 3-3 15 0 18"/></svg>
        </span>
        www.corvanegroup-example.com.au
      </li>
    </ul>

    <div class="band-line"></div>
    <div class="band"></div>
  </section>

</body>
</html>
```